Pier Grove Profile Bacground Needed

I need a simple Pier Grove Background graphic for my Pier Grove profile. My website is www.MeridelVKP.com
I have attached a couple of photos and our logo.

The tag line is: BEAUTY | FUNCTION | ON TIME | ON BUDGET

```html
<!DOCTYPE html>
<html lang="en">
<head>
<meta charset="UTF-8">
<title>Meridel Kitchen &amp; Bath – Pier Grove Banner</title>
<link rel="stylesheet" href="https://fonts.googleapis.com/css2?family=Josefin+Sans:wght@300;600&family=Cormorant+Garamond:wght@600&display=swap">
<style>
  :root {
    --teal: #a8cdca;
    --white: #ffffff;
    --tile-blue: #a9c9d6;
    --sky: #dbe9ef;
    --sea: #7fbfcf;
    --foliage: #93b57e;
    --window-frame: #f4f7f7;
    --vanity: #f6f6f4;
    --floor: #dedbd5;
  }
  * { margin: 0; padding: 0; box-sizing: border-box; }
  html, body { width: 1200px; height: 300px; overflow: hidden; }
  body { background: var(--teal); }
  .banner {
    position: relative;
    width: 1200px;
    height: 300px;
    overflow: hidden;
    background: var(--teal);
  }
  .bathroom-photo {
    position: absolute;
    left: 0; top: 0;
    width: 770px; height: 300px;
    background:
      linear-gradient(90deg, rgba(168,205,202,0) 0%, rgba(168,205,202,0) 82%, var(--teal) 100%),
      linear-gradient(90deg, var(--tile-blue) 0%, rgba(169,201,214,0.6) 22%, rgba(169,201,214,0) 30%),
      linear-gradient(180deg, var(--sky) 0%, var(--sky) 18%, var(--sea) 26%, var(--sea) 32%, var(--foliage) 38%, var(--foliage) 43%, var(--window-frame) 48%, var(--tile-blue) 56%, var(--vanity) 64%, var(--vanity) 82%, var(--floor) 100%);
  }
  .brand {
    position: absolute;
    left: 828px; top: 78px;
    width: 300px;
    color: var(--white);
    font-family: "Josefin Sans", sans-serif;
    font-weight: 300;
    text-align: center;
  }
  .brand-name {
    display: block;
    font-size: 64px;
    letter-spacing: 1px;
    line-height: 1;
  }
  .brand-sub {
    display: block;
    margin-top: 8px;
    font-size: 24px;
    letter-spacing: 4px;
    line-height: 1;
  }
  .tagline {
    position: absolute;
    left: 664px; top: 229px;
    width: 518px;
    text-align: center;
    color: var(--white);
    font-family: "Cormorant Garamond", serif;
    font-weight: 600;
    font-size: 21px;
    letter-spacing: 1.5px;
    line-height: 1;
    white-space: nowrap;
  }
  .website {
    position: absolute;
    left: 664px; top: 263px;
    width: 518px;
    text-align: center;
    color: var(--white);
    font-family: "Josefin Sans", sans-serif;
    font-weight: 600;
    font-size: 15px;
    letter-spacing: 1px;
    line-height: 1;
  }
</style>
</head>
<body>
  <div class="banner">
    <div class="bathroom-photo" role="img" aria-label="Bright coastal bathroom with white freestanding tub, white vanity, blue tile and windows overlooking the ocean and palms"></div>
    <div class="brand">
      <span class="brand-name">MERIDEL</span>
      <span class="brand-sub">KITCHEN &amp; BATH</span>
    </div>
    <p class="tagline">BEAUTY | FUNCTION | ON TIME | ON BUDGET</p>
    <p class="website">www.MeridelVKP.com</p>
  </div>
</body>
</html>
```